Artistic Poster for a Short Film

I am the Writer/Director of an upcoming short film called "Driftwater" and I need a 20x30 poster for the project screening. The screening is coming up very soon so apologies for the quick turnaround time. Here is a short synopsis:

"Walter is a mysterious man who is lost and disoriented. With the help of Marisol, he searches for items out of an old diary written long ago by a woman named Gloria, despite not understanding exactly why he does so. Marisol helps, but when they are unsuccessful she confronts Walter: Does he know why he restlessly searches for these items? The truth is shocking, and reveals Walter's connections to Marisol, Gloria, and the strange old diary.

The truth is that Walter is actually an old man, and Marisol is his caretaker and granddaughter. His memories, including those of Gloria, his deceased wife, have been destroyed by Dementia. He often wakes believing himself to be at an earlier stage of his life, and therefore meets many of the challenges of life with anger and confusion."

Here is the film's website: http://www.driftwater-film.example
Here is our successful Fundbarrow: http://www.fundbarrow.example/projects/502847719/driftwater-a-short-film

The design should be dark and simple. I'm a fan of the art-prints that this short film used (scroll down to see): http://www.fundbarrow.example/projects/ruthvanderlo/kettle-a-short-film-based-on-the-story-by-omar-quill but I'm also open to other ideas. If you google "alternative movie posters" you'll see what I mean. The poster should be simple, easy to read, and hint at the themes of the film without giving the twist away.

Here is a link to the Fine Cut of the film: https://clipvault.example/48210576 The password is: lanterns72
It is not a completed version but will give you an idea of what the film will look like.

Target Market(s)

The intended audience is an art-film crowd of moviegoers.

Industry/Entity Type

Movie

Requirements
Must have
• The poster must have the typical movie poster text at the bottom. The information that should be included is: First line: COPPER LANTERN STUDIOS presents a film by DANIEL OSTROM "DRIFTWATER" MARCEL BRUNAUD TERRA WOLCOTT
Second line: music by OWEN PRATT director of photography VICTOR L. MORALES edited by SIMON ORR costume designer ROBERTA CLINE
Third line: produced by GAIL TORVALD DANIEL OSTROM written and directed by DANIEL OSTROM

It should have the title of the film "Driftwater" and "A film by Daniel Ostrom" on the poster (in addition to the text at the bottom.

It must be high-quality and printable to a size of 20x30. Ideal resolution is 6060x9090. I only need the high quality printable file, I will do the printing myself.
Should not have
• Bright colors.

```html
<!DOCTYPE html>
<html lang="en">
<head>
<meta charset="utf-8">
<title>Driftwater — a film by Daniel Ostrom</title>
<link rel="stylesheet" href="https://fonts.googleapis.com/css2?family=Cormorant+SC:wght@500&family=Tangerine:wght@700&family=Oswald:wght@400&display=swap">
<style>
  :root {
    --bg-deep: #0c0f0a;
    --bg-mid: #161a13;
    --title-brown: #5e4e3f;
    --script-brown: #4a3a2c;
    --credit-ink: #d8d4cc;
    --coat-light: #a8947a;
    --coat-dark: #5a4a38;
  }
  html, body {
    margin: 0;
    padding: 0;
    width: 800px;
    height: 1200px;
    overflow: hidden;
    background: var(--bg-deep);
  }
  .poster {
    position: relative;
    width: 800px;
    height: 1200px;
    overflow: hidden;
    background: radial-gradient(ellipse at 30% 40%, var(--bg-mid) 0%, var(--bg-deep) 75%);
  }
  .portrait {
    position: absolute;
    left: 180px;
    top: 0;
    width: 620px;
    height: 1200px;
    background:
      radial-gradient(ellipse 190px 260px at 560px 330px, #7d6d62 0%, #4c4038 55%, transparent 100%),
      radial-gradient(ellipse 420px 620px at 560px 900px, var(--coat-light) 0%, #8a7860 45%, var(--coat-dark) 75%, transparent 100%);
  }
  .title {
    position: absolute;
    left: 30px;
    top: 22px;
    width: 84px;
    margin: 0;
    font-family: "Cormorant SC", "Times New Roman", serif;
    font-weight: 500;
    font-size: 88px;
    line-height: 91px;
    color: var(--title-brown);
    text-align: center;
  }
  .title span { display: block; }
  .byline {
    position: absolute;
    left: 0;
    right: 0;
    top: 985px;
    margin: 0;
    text-align: center;
    font-family: "Tangerine", cursive;
    font-weight: 700;
    font-size: 62px;
    line-height: 1;
    letter-spacing: 3px;
    color: var(--script-brown);
  }
  .credits {
    position: absolute;
    left: 0;
    right: 0;
    top: 1076px;
    margin: 0;
    text-align: center;
    font-family: "Oswald", "Arial Narrow", sans-serif;
    font-size: 11.5px;
    line-height: 29px;
    letter-spacing: 2.4px;
    color: var(--credit-ink);
    text-transform: uppercase;
  }
  .credits span { display: block; white-space: nowrap; }
</style>
</head>
<body>
  <main class="poster">
    <div class="portrait" role="img" aria-label="Photograph of an elderly man in a tan zip jacket, seated at night against a dark background"></div>

    <h1 class="title" aria-label="Driftwater">
      <span>D</span><span>R</span><span>I</span><span>F</span><span>T</span><span>W</span><span>A</span><span>T</span><span>E</span><span>R</span>
    </h1>

    <p class="byline">a film by Daniel Ostrom</p>

    <p class="credits">
      <span>Copper Lantern Studios presents a film by Daniel Ostrom "Driftwater" Marcel Brunaud Terra</span>
      <span>Wolcott music by Owen Pratt director of photography Victor L. Morales edited by Simon Orr costume</span>
      <span>designer Roberta Cline produced by Gail Torvald Daniel Ostrom written and</span>
      <span>directed by Daniel Ostrom</span>
    </p>
  </main>
</body>
</html>
```